Flyer for our prophetic church event

I need a flyer designed for the launching of our "7 Radiant Harvest Gatherings" event. This event should high light the next 7 Sundays starting on February the 11th, 2018

Event Name:
7 Radiant Harvests

Event Slogan or topic:
Go and tell John ... the blind see, the lame walk, the lepers are cleansed, the deaf hear, the dead are raised,
the poor have the gospel preached to them.

Speaker:
Prophet Marcus Obuya

February 11th
February 18th
February 25th
March 4th
March 11th
March 18th
March 25th

Location:
Talvor Community Center
382 Wendle Street
Portland, ME 04981
United States

Time:
10:00AM - 12:00PM

We welcome you all in the name of Jesus Christ

Contact Info:
Tel:+1(555) 302 1189 - Email:contact@mirovalefold.org - Website: http://velosa.org

Target Market(s)

Young adults

Industry/Entity Type

Church

Font styles to use
Other font styles liked:
• Surprise me, I trust the designers skills

Colors

Designer to choose colors to be used in the design.

Requirements
Must have
• The Velosa logo
• Marcus Obuya's picture
• The
Should not have
• The background of the Marcus Obuya's picture

```html
<!DOCTYPE html>
<html lang="en">
<head>
<meta charset="utf-8">
<title>Seven Radiant Harvests – Flyer</title>
<link rel="stylesheet" href="https://fonts.googleapis.com/css2?family=Bebas+Neue&family=Open+Sans:wght@600;700&display=swap">
<style>
  :root {
    --navy: #0d3a5e;
    --orange: #f7941d;
    --quote-mark: #f9cfa0;
    --white: #ffffff;
    --page-bg: #bdbdbd;
    --sky-top: #6b4a6a;
    --sky-mid: #d9683a;
    --sky-low: #f0a050;
  }
  * { margin: 0; padding: 0; box-sizing: border-box; }
  html, body { width: 917px; height: 1200px; overflow: hidden; }
  body { background: var(--page-bg); font-family: "Open Sans", Arial, sans-serif; position: relative; }

  .flyer {
    position: absolute; left: 87px; top: 75px;
    width: 741px; height: 1045px;
    background: var(--white); overflow: hidden;
  }
  .hero { position: absolute; left: 0; top: 0; width: 741px; height: 520px; }

  .brand {
    position: absolute; left: 65px; top: 0; width: 210px; height: 160px;
    background: var(--navy); border-radius: 0 0 14px 14px;
    display: flex; align-items: center; justify-content: center; gap: 10px;
  }
  .brand-dot { width: 14px; height: 14px; border-radius: 50%; background: var(--orange); }
  .brand-name { color: var(--white); font-weight: 600; font-size: 34px; letter-spacing: 1px; }

  .title-badge {
    position: absolute; left: 224px; top: 225px; width: 294px; height: 294px;
    border-radius: 50%; background: var(--navy); border: 8px solid var(--white);
    display: flex; flex-direction: column; align-items: center; justify-content: center;
    font-family: "Bebas Neue", Impact, sans-serif; font-size: 64px; line-height: 60px;
    color: var(--white); text-align: center;
  }
  .title-badge .accent { color: var(--orange); }

  .verse {
    position: absolute; left: 60px; top: 530px; width: 621px;
    text-align: center; color: var(--navy); font-weight: 700; font-size: 18px; line-height: 25px;
  }
  .quote-mark {
    position: absolute; color: var(--quote-mark); font-family: Georgia, serif;
    font-size: 90px; line-height: 1; font-weight: 700;
  }
  .quote-open { left: 56px; top: 505px; }
  .quote-close { left: 590px; top: 582px; }

  .speaker-photo {
    position: absolute; left: 310px; top: 642px; width: 122px; height: 122px;
    border-radius: 50%; border: 4px solid var(--navy);
    background: radial-gradient(circle at 50% 40%, #8a6a55 0%, #4a3a35 45%, #d8d0c8 100%);
  }
  .speaker-name {
    position: absolute; left: 0; top: 780px; width: 741px; text-align: center;
    color: var(--navy); font-weight: 700; font-size: 16px;
  }

  .details { position: absolute; top: 823px; color: var(--navy); font-weight: 700; font-size: 14px; line-height: 23.5px; }
  .details sup { font-size: 9px; }
  .details-dates { right: 398px; text-align: right; }
  .details-place { left: 398px; }
  .details-divider { position: absolute; left: 369px; top: 825px; width: 2px; height: 70px; background: var(--orange); }

  .welcome-band {
    position: absolute; left: 0; top: 920px; width: 741px; height: 56px;
    background: var(--navy); color: var(--white);
    display: flex; align-items: center; justify-content: center;
    font-weight: 700; font-size: 19px; letter-spacing: 0.3px;
  }
  .contact-band {
    position: absolute; left: 0; top: 976px; width: 741px; height: 69px;
    background: var(--orange); color: var(--navy);
    display: flex; align-items: center; justify-content: space-between;
    padding: 0 84px 0 56px; font-weight: 700; font-size: 15px;
  }
  .contact-item { display: flex; align-items: center; gap: 8px; }
  .contact-icon { width: 16px; height: 16px; }
</style>
</head>
<body>
<main class="flyer">
  <svg class="hero" viewBox="0 0 741 520" aria-hidden="false">
    <defs>
      <linearGradient id="sky" x1="0" y1="0" x2="0" y2="1">
        <stop offset="0" stop-color="var(--sky-top)"/>
        <stop offset="0.45" stop-color="var(--sky-mid)"/>
        <stop offset="1" stop-color="var(--sky-low)"/>
      </linearGradient>
    </defs>
    <rect role="img" aria-label="Sunset sky with a wooden cross draped in purple cloth" x="0" y="0" width="741" height="470" fill="url(#sky)"/>
    <path d="M0,300 C110,330 220,355 320,362 L320,450 L0,450 Z" fill="var(--white)"/>
    <path d="M0,308 C110,338 220,362 320,370 L320,440 C200,447 90,448 0,446 Z" fill="var(--orange)"/>
    <path d="M741,162 L741,262 C670,300 590,322 500,338 L500,318 C600,290 680,240 741,162 Z" fill="var(--navy)"/>
    <path d="M741,262 L741,272 C670,312 590,335 500,348 L500,338 C590,322 670,300 741,262 Z" fill="var(--white)"/>
    <path d="M741,272 L741,292 C670,340 590,375 500,400 L500,375 C590,350 670,315 741,272 Z" fill="var(--orange)"/>
    <path d="M0,446 C90,448 200,447 320,440 L500,400 C590,375 670,340 741,292 L741,520 L0,520 Z" fill="var(--white)"/>
  </svg>

  <div class="brand">
    <span class="brand-dot"></span>
    <span class="brand-name">VELOSA</span>
  </div>

  <h1 class="title-badge">
    <span>SEVEN</span>
    <span class="accent">RADIANT</span>
    <span>HARVESTS</span>
  </h1>

  <span class="quote-mark quote-open">&ldquo;</span>
  <p class="verse">Go and tell John ... the blind see, the lame walk, the lepers are cleansed, the deaf hear, the dead are raised, the poor have the gospel preached to them.</p>
  <span class="quote-mark quote-close">&rdquo;</span>

  <div class="speaker-photo" role="img" aria-label="Portrait photo of Prophet Marcus Obuya"></div>
  <p class="speaker-name">Prophet Marcus Obuya</p>

  <p class="details details-dates">February 11<sup>th</sup> to 25<sup>th</sup><br>March 4<sup>th</sup> to 25<sup>th</sup><br>10:00AM - 12:00PM</p>
  <span class="details-divider"></span>
  <p class="details details-place">Talvor Community Center<br>382 Wendle Street, Portland,<br>ME 04981, United States</p>

  <div class="welcome-band">WE WELCOME YOU ALL IN THE NAME OF JESUS CHRIST</div>

  <footer class="contact-band">
    <span class="contact-item">
      <svg class="contact-icon" viewBox="0 0 16 16"><circle cx="8" cy="8" r="8" fill="var(--white)"/><path d="M5.2,4 L6.6,4 L7.2,6 L6.3,6.8 C6.8,7.9 7.9,9 9,9.5 L9.8,8.6 L11.8,9.2 L11.8,10.6 C11.8,11.2 11.2,11.7 10.6,11.6 C7.4,11.2 4.6,8.4 4.2,5.2 C4.1,4.6 4.6,4 5.2,4 Z" fill="var(--navy)"/></svg>
      +1(555) 302 1189
    </span>
    <span class="contact-item">
      <svg class="contact-icon" viewBox="0 0 16 16"><circle cx="8" cy="8" r="8" fill="var(--white)"/><rect x="4.3" y="5.3" width="7.4" height="5.4" fill="var(--navy)"/><path d="M4.3,5.3 L8,8.2 L11.7,5.3" fill="none" stroke="var(--white)" stroke-width="0.8"/></svg>
      contact@mirovalefold.org
    </span>
    <span class="contact-item">
      <svg class="contact-icon" viewBox="0 0 16 16"><circle cx="8" cy="8" r="8" fill="var(--white)"/><circle cx="8" cy="8" r="4" fill="none" stroke="var(--navy)" stroke-width="1"/><path d="M4,8 H12 M8,4 C6,6 6,10 8,12 M8,4 C10,6 10,10 8,12" fill="none" stroke="var(--navy)" stroke-width="0.8"/></svg>
      www.velosa.org
    </span>
  </footer>
</main>
</body>
</html>
```